Stationery design for a hip Muslim Travel Agency

We are looking for a colorful and energetic stationery design for a Muslim tour and travel agency. We need a letterhead, A4 folder, business card and loyalty card design.

The designs should be clean and cheerful and have a feeling of a colorful mosaic in a mosque. You can use the Facebook avatar and cover photo as the basis.

Rimbelu card is a loyalty card we issue to our clients. This can have a similar feel to the business card and it should NOT have the word "card" added to the logo. Think of airline membership cards.

Target Market(s)

Indonesians, 25-44 years old, Muslim, interesting in Umroh and Haji and other Muslim tours.

Industry/Entity Type

Travel Agent

Contact Information for Business Card

As provided in the .psd file.

Font styles to use
Sans Serif

Colors
27a0d5
33b8a4
00a990
0492cd

Requirements
Must have
• Letterhead design
• A4 folder design
• Business card
• Loyalty card (without the word "card" in the logo)
Nice to have
• Use the mosaic patterns provided in the files. We want to express the theme of colorful Islam.
Should not have
• Don't copy the .psd files provided in the brief. This is just for the content, those files were not prepared by a designer.

```html
<!DOCTYPE html>
<html lang="en">
<head>
<meta charset="utf-8">
<title>Rimbelu stationery set</title>
<link href="https://fonts.googleapis.com/css2?family=Lato:wght@400;700;900&family=Share+Tech+Mono&display=swap" rel="stylesheet">
<style>
  :root{
    --bg:#d2d3d5;
    --paper:#ffffff;
    --green:#8dc63f;
    --green-light:#a3d14a;
    --ink:#1d1d1b;
    --teal:#1db39c;
    --grey-text:#6d6e71;
    --stripe:#1a1a1a;
  }
  *{margin:0;padding:0;box-sizing:border-box}
  html,body{width:1200px;height:1200px;overflow:hidden;background:var(--bg);font-family:"Lato",sans-serif;color:var(--ink)}
  .canvas{position:relative;width:1200px;height:1200px}
  .piece{position:absolute}
  .shadow{box-shadow:0 3px 6px rgba(0,0,0,.18)}
  .pattern{background:linear-gradient(135deg,var(--green-light),var(--green))}
  .brand{font-family:"Lato",sans-serif;font-weight:900;color:var(--ink);display:flex;align-items:center;gap:6px;white-space:nowrap}
  .brand .dot{display:inline-block;border-radius:50%;background:var(--teal)}
  .brand.light{color:#fff}
  .brand.light .dot{background:#fff}

  /* folder */
  .folder-svg{position:absolute;left:0;top:0}
  .folder-panel{left:279px;top:84px;width:322px;height:456px}
  .folder-cover{left:601px;top:84px;width:322px;height:456px;background:var(--paper);display:flex;align-items:center;justify-content:center}
  .folder-cover .brand{font-size:27px;gap:10px}
  .folder-cover .dot{width:22px;height:22px}
  .folder-contacts{position:absolute;left:0;right:0;top:402px;display:flex;justify-content:space-around;padding:0 22px;color:#fff;font-size:5px}
  .folder-contacts div{display:flex;flex-direction:column;align-items:center;gap:5px}

  /* letterhead */
  .letterhead{left:188px;top:670px;width:322px;height:454px;background:var(--paper)}
  .letterhead .brand{position:absolute;left:38px;top:46px;font-size:14px}
  .letterhead .dot{width:11px;height:11px}
  .lh-contact{position:absolute;right:14px;top:44px;font-size:3.6px;color:var(--grey-text);line-height:6.9px;text-align:right}
  .lh-contact span{display:inline-block;width:3px;height:3px;border-radius:50%;background:var(--teal);margin-left:4px;vertical-align:middle}
  .lh-body{position:absolute;left:37px;top:117px;width:249px;font-size:4.6px;line-height:6.2px;color:var(--grey-text)}
  .lh-body p{margin-bottom:9px;text-align:justify}
  .lh-body .salute{color:var(--ink);margin-bottom:24px}
  .lh-body .strong{font-weight:700;color:var(--ink)}
  .lh-sign{position:absolute;left:37px;top:330px;width:47px;border-bottom:1px solid #444}
  .lh-band{position:absolute;left:0;bottom:0;width:100%;height:26px}

  /* business card */
  .bc-front{left:491px;top:742px;width:201px;height:114px;display:flex;align-items:center;justify-content:center}
  .bc-front .brand{font-size:17px}
  .bc-front .dot{width:13px;height:13px}
  .bc-back{left:491px;top:880px;width:201px;height:115px;background:var(--paper)}
  .bc-name{position:absolute;left:23px;top:18px;font-family:"Share Tech Mono",monospace;font-size:7.5px;font-weight:700}
  .bc-role{position:absolute;left:23px;top:27px;font-size:5px;color:var(--teal)}
  .bc-lines{position:absolute;left:23px;top:58px;font-size:4.6px;line-height:8.5px;color:var(--ink)}
  .bc-lines i{display:inline-block;width:3px;height:3px;border-radius:50%;background:var(--teal);margin-right:4px;vertical-align:middle}
  .bc-addr{position:absolute;left:23px;top:93px;font-size:4.6px}
  .bc-addr i{display:inline-block;width:3px;height:3px;border-radius:50%;background:var(--teal);margin-right:4px;vertical-align:middle}
  .bc-strip{position:absolute;right:0;top:0;width:40px;height:100%;display:flex;align-items:center;justify-content:center}
  .bc-strip .brand{transform:rotate(90deg);font-size:10px}
  .bc-strip .dot{width:7px;height:7px}

  /* loyalty card */
  .lc-front{left:747px;top:738px;width:193px;height:123px;border-radius:6px;color:#fff}
  .lc-front .brand{position:absolute;left:16px;top:12px;font-size:12px}
  .lc-front .dot{width:10px;height:10px}
  .lc-title{position:absolute;left:16px;top:52px;font-family:"Share Tech Mono",monospace;font-size:10px;font-weight:700}
  .lc-number{position:absolute;left:16px;top:68px;font-family:"Share Tech Mono",monospace;font-size:7px;letter-spacing:.6px}
  .lc-valid{position:absolute;left:72px;top:79px;width:74px;text-align:right;font-size:4px}
  .lc-holder{position:absolute;left:16px;top:101px;font-family:"Share Tech Mono",monospace;font-size:7px}
  .lc-back{left:829px;top:838px;width:193px;height:122px;background:var(--paper);border-radius:6px;text-align:center}
  .lc-stripe{position:absolute;left:0;top:14px;width:100%;height:21px;background:var(--stripe)}
  .lc-intro{position:absolute;left:0;right:0;top:43px;font-size:4px}
  .lc-head{position:absolute;left:0;right:0;top:53px;font-family:"Share Tech Mono",monospace;font-size:10px;font-weight:700}
  .lc-text{position:absolute;left:18px;right:18px;top:72px;font-size:4px;line-height:5.2px}
  .lc-contacts{position:absolute;left:20px;right:20px;top:101px;display:flex;justify-content:space-between;font-size:3.6px}
  .lc-contacts i{display:inline-block;width:3px;height:3px;border-radius:50%;background:var(--teal);margin-right:3px;vertical-align:middle}
</style>
</head>
<body>
<main class="canvas">

  <!-- A4 folder -->
  <svg class="folder-svg" width="1200" height="1200" aria-hidden="true">
    <polygon points="216,122 279,84 279,540 216,494" fill="#ffffff"/>
    <polygon points="279,540 601,540 548,617 279,617" fill="#ffffff"/>
  </svg>
  <section class="piece folder-panel pattern" role="img" aria-label="Green mosque mosaic pattern">
    <div class="folder-contacts">
      <div>
        <svg width="8" height="8" viewBox="0 0 24 24"><path fill="#fff" d="M6.6 10.8a15 15 0 0 0 6.6 6.6l2.2-2.2a1 1 0 0 1 1-.25 11.4 11.4 0 0 0 3.6.57 1 1 0 0 1 1 1V20a1 1 0 0 1-1 1A17 17 0 0 1 3 4a1 1 0 0 1 1-1h3.5a1 1 0 0 1 1 1c0 1.25.2 2.45.57 3.6a1 1 0 0 1-.25 1z"/></svg>
        <span>+0123 45678</span>
      </div>
      <div>
        <svg width="8" height="8" viewBox="0 0 24 24"><path fill="#fff" d="M2 5h20v14H2zm2 2v.5l8 5 8-5V7z"/></svg>
        <span>info@rimbelu.id</span>
      </div>
      <div>
        <svg width="8" height="8" viewBox="0 0 24 24"><path fill="#fff" d="M12 2a7 7 0 0 0-7 7c0 5 7 13 7 13s7-8 7-13a7 7 0 0 0-7-7zm0 9.5A2.5 2.5 0 1 1 12 6.5a2.5 2.5 0 0 1 0 5z"/></svg>
        <span>18 Jalan Melati, Bandung 40115</span>
      </div>
    </div>
  </section>
  <section class="piece folder-cover">
    <div class="brand"><span class="dot"></span>rimbelu.id</div>
  </section>

  <!-- Letterhead -->
  <section class="piece letterhead shadow">
    <div class="brand"><span class="dot"></span>rimbelu.id</div>
    <div class="lh-contact">
      +0123 45678<span></span><br>
      info@rimbelu.id<span></span><br>
      www.rimbelu.id<span></span><br>
      18 Jalan Melati, Bandung 40115<span></span>
    </div>
    <div class="lh-body">
      <p class="salute">Dear, Mr________</p>
      <p>Lorem Ipsum is simply dummy text of the printing and typesetting industry. Lorem Ipsum has been the industry's standard dummy text ever since the 1500s, when an unknown printer took a galley of type and scrambled it to make a type specimen book. It has survived not only five centuries, but also the leap into electronic typesetting, remaining essentially unchanged. It was popularised in the 1960s with the release of transfer sheets containing Lorem Ipsum passages, and more recently with desktop publishing software including many versions of Lorem Ipsum.</p>
      <p>Lorem Ipsum is simply dummy text of the printing and typesetting industry. Lorem Ipsum has been the industry's standard dummy text ever since the 1500s, when an unknown printer took a galley of type and scrambled it to make a type specimen book. It has survived not only five centuries, but also the leap into electronic typesetting, remaining essentially unchanged. It was popularised in the 1960s with the release of transfer sheets containing Lorem Ipsum passages, and more recently with desktop publishing software including many versions of Lorem Ipsum.</p>
      <p class="strong">Lorem Ipsum is simply dummy text of the printing and typesetting industry. Lorem Ipsum has been the industry's standard dummy text ever since the 1500s, when an unknown printer took a galley of type and scrambled it to make a type specimen book.</p>
      <p>Lorem Ipsum is simply dummy text of the printing and typesetting industry. Lorem Ipsum has been the industry's standard dummy text ever since the 1500s, when an unknown printer took a galley of type and scrambled it to make a type specimen book.</p>
    </div>
    <div class="lh-sign" role="img" aria-label="Signature line"></div>
    <div class="lh-band pattern" role="img" aria-label="Green mosaic pattern band"></div>
  </section>

  <!-- Business card -->
  <section class="piece bc-front pattern shadow" role="img" aria-label="Green mosaic pattern with brand name">
    <div class="brand light"><span class="dot"></span>rimbelu.id</div>
  </section>
  <section class="piece bc-back shadow">
    <div class="bc-name">Dimas Wiratama</div>
    <div class="bc-role">Director</div>
    <div class="bc-lines">
      <div><i></i>+0123 45678</div>
      <div><i></i>info@rimbelu.id</div>
      <div><i></i>www.rimbelu.id</div>
    </div>
    <div class="bc-addr"><i></i>18 Jalan Melati, Bandung 40115</div>
    <div class="bc-strip pattern" role="img" aria-label="Green mosaic pattern strip">
      <div class="brand light"><span class="dot"></span>rimbelu.id</div>
    </div>
  </section>

  <!-- Loyalty card -->
  <section class="piece lc-front pattern shadow" role="img" aria-label="Loyalty card front on green mosaic pattern">
    <div class="brand light"><span class="dot"></span>rimbelu.id</div>
    <div class="lc-title">Loyalty</div>
    <div class="lc-number">0123 4567 8901 2345</div>
    <div class="lc-valid">Valid 07/18</div>
    <div class="lc-holder">Lorem Ipsum</div>
  </section>
  <section class="piece lc-back shadow">
    <div class="lc-stripe"></div>
    <div class="lc-intro">Lorem Ipsum is simply dummy text of the printing and typesetting industry.</div>
    <div class="lc-head">Lorem Ipsum</div>
    <div class="lc-text">Lorem Ipsum is simply dummy text of the printing and typesetting industry. Lorem Ipsum has been the industry's standard dummy text ever since the 1500s, when an unknown printer took a galley of type and scrambled it to make a type specimen book.</div>
    <div class="lc-contacts">
      <span><i></i>+0123 45678</span>
      <span><i></i>info@rimbelu.id</span>
    </div>
  </section>

</main>
</body>
</html>
```